依頼詳細
デザインについては、下記WEBサイトに掲載されているような
スタイリッシュかつシンプルなものが理想です。

URL: https://kinpa-morimeshi.com/contents/column/nengajyou-seisakujirei-2019/

・本来は箔押しで作成予定でしたが、納期の関係で難しいかと思っております。デザインの参考としてご確認ください。

・デザインによってはフチなし印刷の発注は可能です。

またロゴを添付しておりますが、デザイン作成に際しての
色の編集、文字部分の切り取り等は自由にしていただいて結構です。

```html
<!DOCTYPE html>
<html lang="ja">
<head>
<meta charset="utf-8">
<title>2021 年賀状</title>
<link href="https://fonts.googleapis.com/css2?family=Montserrat:wght@300;500&family=Noto+Sans+JP:wght@400;700&family=Noto+Serif+JP:wght@500&display=swap" rel="stylesheet">
<style>
  :root {
    --paper: #ffffff;
    --ink: #1d1d1d;
    --logo-grey: #4a4a4a;
    --greeting-red: #d2232a;
    --gold-dark: #6b5420;
    --gold-mid: #a88a3e;
    --gold-light: #e6cf8a;
    --photo-light: #d6d6d6;
    --photo-mid: #6e6e6e;
    --photo-dark: #161616;
  }
  * { margin: 0; padding: 0; box-sizing: border-box; }
  html, body { width: 813px; height: 1200px; overflow: hidden; background: var(--paper); }
  .card {
    position: relative;
    width: 813px;
    height: 1200px;
    background: var(--paper);
    font-family: "Noto Sans JP", sans-serif;
    color: var(--ink);
  }
  .brand {
    position: absolute;
    left: 100px;
    top: 112px;
    display: flex;
    align-items: center;
    gap: 10px;
  }
  .brand-square {
    width: 18px;
    height: 18px;
    background: var(--logo-grey);
  }
  .brand-name {
    font-weight: 400;
    font-size: 15px;
    letter-spacing: 0.04em;
    color: var(--logo-grey);
  }
  .greeting {
    position: absolute;
    right: 70px;
    top: 56px;
    writing-mode: vertical-rl;
    font-family: "Noto Serif JP", serif;
    font-weight: 500;
    font-size: 24px;
    letter-spacing: 0.1em;
    color: var(--greeting-red);
  }
  .gold-band {
    position: absolute;
    left: 0;
    top: 812px;
    width: 813px;
    height: 288px;
    background: linear-gradient(90deg, var(--gold-dark) 0%, var(--gold-mid) 55%, var(--gold-dark) 100%);
  }
  .figure-photo {
    position: absolute;
    left: 150px;
    top: 150px;
    width: 500px;
    height: 950px;
    background: linear-gradient(180deg, var(--photo-light) 0%, var(--photo-mid) 35%, var(--photo-dark) 70%, var(--photo-dark) 100%);
  }
  .year-block {
    position: absolute;
    left: 0;
    top: 820px;
    width: 813px;
    text-align: center;
  }
  .year {
    font-family: "Montserrat", sans-serif;
    font-weight: 500;
    font-size: 140px;
    line-height: 1;
    letter-spacing: -0.02em;
    background: linear-gradient(180deg, #fff4c8 0%, var(--gold-light) 45%, #b8913a 100%);
    -webkit-background-clip: text;
    background-clip: text;
    color: transparent;
  }
  .new-year {
    margin-top: 12px;
    font-family: "Montserrat", sans-serif;
    font-weight: 300;
    font-size: 27px;
    letter-spacing: 0.16em;
    color: var(--gold-light);
  }
  .representative {
    position: absolute;
    right: 62px;
    top: 1060px;
    font-size: 14px;
    color: #f4f4f4;
    letter-spacing: 0.05em;
  }
  .representative .role { font-size: 11px; margin-right: 10px; }
  .company {
    position: absolute;
    left: 40px;
    top: 1112px;
    width: 740px;
  }
  .company-name {
    font-weight: 700;
    font-size: 16px;
    letter-spacing: 0.02em;
  }
  .company-address {
    margin-top: 6px;
    font-size: 12px;
    letter-spacing: 0.02em;
  }
</style>
</head>
<body>
  <main class="card">
    <div class="brand">
      <span class="brand-square"></span>
      <span class="brand-name">NOVA STRIDE INC.</span>
    </div>

    <p class="greeting">本年も宜しくお願い申し上げます</p>

    <div class="gold-band"></div>
    <div class="figure-photo" role="img" aria-label="スーツを着た牛頭の人物のモノクロ写真"></div>

    <div class="year-block">
      <p class="year">2021</p>
      <p class="new-year">HAPPY NEW YEAR</p>
    </div>

    <p class="representative"><span class="role">代表取締役</span>森川 拓海</p>

    <footer class="company">
      <p class="company-name">株式会社ノヴァストライド（NOVA STRIDE INC.）</p>
      <p class="company-address">〒530-0099 大阪市北区架空町2丁目3-45 サンプル中央ビル5F　Tel.06-0000-1234 Fax.06-0000-1235</p>
    </footer>
  </main>
</body>
</html>
```